Travel Agency Website - Simple General

Need a 7 page simple design that is pretty repetitive. Need to be able to load quickly that is SEO optimized. Trying to give ideas on what they can do, be personal as we are local, but at the same time come across as professional and get information easily with little burden.

- Landing Page
- Marrowind Vacations Page
- Family Trips
- Road Trips from Texas
- Other Destinations
- About Us Page
- Contact Us Page

Target Market(s)

Families

Coding

Coded - Design and coding required

Number of Pages Required

5+ page

Colors

Designer to choose colors to be used in the design.

Requirements
Must have
• Like it to flow easily with our logo. Use that for colors, etc.

```html
<!DOCTYPE html>
<html lang="en">
<head>
<meta charset="utf-8">
<title>Contact Us | Harbor Lane Travel Co.</title>
<link href="https://fonts.googleapis.com/css2?family=Poppins:wght@400;500;700&display=swap" rel="stylesheet">
<style>
:root{
  --teal:#0b4a5b;
  --teal-dark:#054a5c;
  --gold:#b8832f;
  --panel:#f7f7f7;
  --line:#d9dde0;
  --white:#ffffff;
}
*{box-sizing:border-box;margin:0;padding:0}
html,body{width:994px;height:1200px;overflow:hidden;background:var(--white);font-family:"Poppins",sans-serif;color:var(--teal)}
.page{position:relative;width:994px;height:1200px}
.topbar{position:absolute;left:0;top:0;width:994px;height:52px;background:linear-gradient(90deg,#e4e4e0,#ededea 50%,#e2e2de)}
.topbar-phone{position:absolute;left:157px;top:17px;display:flex;align-items:center;gap:5px;font-weight:500;font-size:13px;color:var(--teal)}
.brand{position:absolute;left:447px;top:8px;width:100px;height:46px;display:flex;align-items:center;justify-content:center;gap:4px;background:var(--white);border-radius:8px;font-weight:700;font-size:9px;color:var(--teal);text-align:center;line-height:1.1;z-index:2}
.brand-dot{width:8px;height:8px;border-radius:50%;background:var(--gold);flex:none}
.social-top{position:absolute;top:21px;display:flex;gap:23px;left:788px}
.social-top span{width:12px;height:12px;border:1.5px solid var(--gold)}
.social-top span:first-child{border-radius:50%}
.social-top span:last-child{border-radius:3px}
.nav{position:absolute;left:0;top:52px;width:994px;height:38px;background:var(--gold)}
.nav::before,.nav::after{content:"";position:absolute;left:0;right:0;border-top:1px dashed rgba(255,255,255,.75)}
.nav::before{top:5px}.nav::after{top:36px}
.nav ul{list-style:none;display:flex;justify-content:center;gap:26px;padding-top:15px;padding-left:4px}
.nav li{font-size:9px;color:var(--white);letter-spacing:.1px}
.hero{position:absolute;left:0;top:90px;width:994px;height:270px;background:linear-gradient(180deg,#8d8a86 0%,#b4a59a 22%,#8aa3a3 34%,#5c9498 50%,#9aa8a6 72%,#b8aa9a 90%,#a9a59d 100%)}
.hero-photo{position:absolute;inset:0}
.hero h1{position:absolute;top:94px;width:100%;text-align:center;color:var(--white);font-weight:700;font-size:26px}
.hero p{position:absolute;top:137px;width:100%;text-align:center;color:var(--white);font-size:8px}
.info-card{position:absolute;top:443px;height:54px;background:var(--panel);border-radius:14px;display:flex;align-items:center}
.info-card .icon{width:32px;height:32px;border-radius:50%;background:var(--gold);display:flex;align-items:center;justify-content:center;margin-left:20px;margin-right:10px}
.info-card h3{font-size:16px;font-weight:700;line-height:1.1}
.info-card p{font-size:12.5px;line-height:1.3}
.card-phone{left:149px;width:145px}
.card-email{left:306px;width:307px}
.card-email .icon{margin-right:13px}
.form-panel{position:absolute;left:149px;top:507px;width:697px;height:473px;background:var(--panel);border-radius:17px}
.form-title{position:absolute;left:20px;top:27px;width:654px;height:50px;background:var(--teal);border-radius:14px;color:var(--white);font-weight:700;font-size:17px;display:flex;align-items:center;justify-content:center}
.field{position:absolute;left:27px;width:651px;background:var(--white);border:1px solid var(--line);border-radius:7px;font-size:8.5px;padding-left:15px;display:flex;align-items:center;color:var(--teal)}
.field.area{align-items:flex-start;padding-top:15px}
.submit{position:absolute;left:20px;top:400px;width:658px;height:51px;background:var(--gold);border-radius:17px;color:var(--white);font-weight:700;font-size:17px;display:flex;align-items:center;justify-content:center}
.footer{position:absolute;left:0;top:1045px;width:994px;height:155px;background:var(--teal-dark);color:var(--white)}
.footer-brand{position:absolute;left:126px;top:29px;width:117px;height:100px;display:flex;align-items:center;justify-content:center;gap:5px;background:var(--white);border-radius:14px;color:var(--teal);font-weight:700;font-size:12px;text-align:center;line-height:1.15}
.footer-contact{position:absolute;left:367px;top:54px;display:flex;align-items:center;font-size:8.5px}
.footer-contact .sep{width:1px;height:18px;background:rgba(255,255,255,.25);margin:0 23px 0 24px}
.footer-contact span{display:flex;align-items:center;gap:5px}
.footer-social{position:absolute;left:841px;top:53px;display:flex;gap:5px}
.footer-social span{width:15px;height:15px;border-radius:50%;background:var(--gold)}
.footer-rule{position:absolute;left:358px;top:85px;width:528px;height:1px;background:rgba(255,255,255,.2)}
.copyright{position:absolute;left:367px;top:96px;font-size:8.5px}
.legal{position:absolute;right:108px;top:96px;font-size:8.5px;display:flex;gap:7px}
</style>
</head>
<body>
<div class="page">
  <header class="topbar">
    <div class="topbar-phone">
      <svg width="13" height="13" viewBox="0 0 24 24"><path fill="#b8832f" d="M6.6 10.8a15 15 0 0 0 6.6 6.6l2.2-2.2c.3-.3.7-.4 1-.2 1.1.4 2.3.6 3.6.6.6 0 1 .4 1 1V20c0 .6-.4 1-1 1A17 17 0 0 1 3 4c0-.6.4-1 1-1h3.5c.6 0 1 .4 1 1 0 1.3.2 2.5.6 3.6.1.3 0 .7-.2 1z"/></svg>
      111.111.1111
    </div>
    <div class="brand"><span class="brand-dot"></span>Harbor Lane<br>Travel Co.</div>
    <div class="social-top" aria-label="Social links"><span></span><span></span></div>
  </header>
  <nav class="nav">
    <ul>
      <li>HOME</li><li>MARROWIND VACATIONS</li><li>FAMILY TRIPS</li><li>TEXAS ROAD TRIPS</li><li>OTHER DESTINATIONS</li><li>ABOUT US</li><li>CONTACT</li>
    </ul>
  </nav>
  <section class="hero">
    <div class="hero-photo" role="img" aria-label="Beach at sunset with waves rolling onto the sand"></div>
    <h1>Contact Us</h1>
    <p>We’d love to hear from you. Let’s plan your next unforgettable trip together.</p>
  </section>

  <div class="info-card card-phone">
    <div class="icon"><svg width="9" height="9" viewBox="0 0 24 24"><path fill="#fff" d="M6.6 10.8a15 15 0 0 0 6.6 6.6l2.2-2.2c.3-.3.7-.4 1-.2 1.1.4 2.3.6 3.6.6.6 0 1 .4 1 1V20c0 .6-.4 1-1 1A17 17 0 0 1 3 4c0-.6.4-1 1-1h3.5c.6 0 1 .4 1 1 0 1.3.2 2.5.6 3.6.1.3 0 .7-.2 1z"/></svg></div>
    <div><h3>Phone</h3><p>111.111.1111</p></div>
  </div>
  <div class="info-card card-email">
    <div class="icon"><svg width="9" height="9" viewBox="0 0 24 24"><path fill="#fff" d="M2 5h20v14H2z"/><path fill="none" stroke="#b8832f" stroke-width="2" d="M2 6l10 7 10-7"/></svg></div>
    <div><h3>Email</h3><p>hello@harborlanetravel.com</p></div>
  </div>

  <section class="form-panel">
    <h2 class="form-title">Get in Touch</h2>
    <div class="field" style="top:93px;height:43px">Name</div>
    <div class="field" style="top:146px;height:42px">Email</div>
    <div class="field" style="top:199px;height:43px">Phone</div>
    <div class="field area" style="top:252px;height:136px">Any details you want us to know?</div>
    <div class="submit">Submit Trip Request</div>
  </section>

  <footer class="footer">
    <div class="footer-brand"><span class="brand-dot"></span>Harbor Lane<br>Travel Co.</div>
    <div class="footer-contact">
      <span><svg width="8" height="8" viewBox="0 0 24 24"><path fill="#fff" d="M6.6 10.8a15 15 0 0 0 6.6 6.6l2.2-2.2c.3-.3.7-.4 1-.2 1.1.4 2.3.6 3.6.6.6 0 1 .4 1 1V20c0 .6-.4 1-1 1A17 17 0 0 1 3 4c0-.6.4-1 1-1h3.5c.6 0 1 .4 1 1 0 1.3.2 2.5.6 3.6.1.3 0 .7-.2 1z"/></svg>111.111.1111</span>
      <i class="sep"></i>
      <span><svg width="8" height="8" viewBox="0 0 24 24"><path fill="#fff" d="M2 5h20v14H2z"/><path fill="none" stroke="#054a5c" stroke-width="2" d="M2 6l10 7 10-7"/></svg>hello@harborlanetravel.com</span>
    </div>
    <div class="footer-social" aria-label="Social links"><span></span><span></span></div>
    <div class="footer-rule"></div>
    <p class="copyright">2026 Harbor Lane Travel Co. All Right Reserved</p>
    <p class="legal"><span>Terms &amp;</span><span>|</span><span>Conditions</span><span>|</span><span>Privacy Policy</span></p>
  </footer>
</div>
</body>
</html>
```